Bright Tooth Dentistry Business Card

We need business cards for our dental office.
We are looking for a clean, elegant design

We provide dental services to children.
Our card needs to be appealing to referring dentists, parents and our team

Target Market(s)

referring dentists, parents and our team

Industry/Entity Type

Dental Clinic

Contact Information for Business Card

4816 Juniper Lane, Suite 100
Cedar Hollow, PA 15237

412-837-2961 Voice
412-837-2962 fax
info@brighttoothdentalpa.com email
www.brighttoothdentalpa.com web

Font styles to use
Sans Serif

Requirements
Must have
• White background - clean, crisp, elegant, simple
• rounded corners
• different color palate - once we come up with design, we will replace the blue with orange, green,
Nice to have
• Follow our logo typeface and colors
• then we can replace color

```html
<!DOCTYPE html>
<html lang="en">
<head>
<meta charset="utf-8">
<title>Bright Tooth Dentistry – Business Card</title>
<link href="https://fonts.googleapis.com/css2?family=Arimo:wght@400;600&display=swap" rel="stylesheet">
<style>
  :root {
    --backdrop: #e2e2e2;
    --brand-blue: #17abe3;
    --card-white: #ffffff;
    --text-grey: #555555;
    --icon-grey: #9c9c9c;
  }
  * { margin: 0; padding: 0; box-sizing: border-box; }
  html, body {
    width: 1200px;
    height: 800px;
    overflow: hidden;
    background: var(--backdrop);
    font-family: "Arimo", Arial, sans-serif;
  }
  .canvas {
    position: relative;
    width: 1200px;
    height: 800px;
    display: flex;
    align-items: center;
    justify-content: center;
    gap: 40px;
  }
  .card {
    position: relative;
    width: 500px;
    height: 286px;
    border-radius: 24px;
    background: var(--brand-blue);
    overflow: hidden;
    box-shadow: 0 10px 28px rgba(0, 0, 0, 0.12);
  }
  .card__face {
    position: absolute;
    top: 0;
    bottom: 0;
    left: 44px;
    right: 44px;
    background: var(--card-white);
    border-radius: 44px;
  }

  /* Front */
  .card--front .card__face {
    display: flex;
    align-items: center;
    justify-content: center;
  }
  .brand-name {
    font-weight: 600;
    font-size: 31px;
    letter-spacing: 0.5px;
    color: var(--brand-blue);
    white-space: nowrap;
  }

  /* Back */
  .contact-list {
    position: absolute;
    left: 44px;
    top: 46px;
    list-style: none;
  }
  .contact-item {
    display: flex;
    align-items: flex-start;
    gap: 14px;
    font-size: 14.5px;
    line-height: 19px;
    color: var(--text-grey);
  }
  .contact-item + .contact-item { margin-top: 14px; }
  .contact-item--online { margin-top: 44px !important; }
  .contact-address { font-style: normal; }
  .contact-icons {
    display: flex;
    flex-direction: column;
    gap: 3px;
    width: 18px;
    padding-top: 2px;
  }
  .contact-icons svg { display: block; width: 16px; height: 16px; fill: var(--icon-grey); }
</style>
</head>
<body>
  <main class="canvas">

    <section class="card card--front" aria-label="Card front">
      <div class="card__face">
        <h1 class="brand-name">Bright Tooth Dentistry</h1>
      </div>
    </section>

    <section class="card card--back" aria-label="Card back">
      <div class="card__face">
        <ul class="contact-list">
          <li class="contact-item">
            <span class="contact-icons">
              <svg viewBox="0 0 16 16" aria-hidden="true"><path d="M8 1a5 5 0 0 0-5 5c0 3.6 5 9 5 9s5-5.4 5-9a5 5 0 0 0-5-5zm0 7a2 2 0 1 1 0-4 2 2 0 0 1 0 4z"/></svg>
            </span>
            <address class="contact-address">4816 Juniper Lane, Suite 100<br>Cedar Hollow, PA 15237</address>
          </li>
          <li class="contact-item">
            <span class="contact-icons">
              <svg viewBox="0 0 16 16" aria-hidden="true"><path d="M3.5 1.5l2.2-.3 1.3 3-1.5 1.2a8 8 0 0 0 4.1 4.1l1.2-1.5 3 1.3-.3 2.2c-.2 1-1.1 1.6-2.1 1.5C6.5 12.5 2.5 8.5 2 4.6c-.1-1 .5-1.9 1.5-3.1z"/></svg>
            </span>
            <span>412-837-2961 Voice<br>412-837-2962 fax</span>
          </li>
          <li class="contact-item contact-item--online">
            <span class="contact-icons">
              <svg viewBox="0 0 16 16" aria-hidden="true"><path d="M1 3h14v10H1zM2.5 4.5 8 9l5.5-4.5v-.1h-11z" fill-rule="evenodd"/></svg>
              <svg viewBox="0 0 16 16" aria-hidden="true"><path d="M2 2l11 4.5-4.3 1.3 4.6 4.6-1.4 1.4-4.6-4.6L6.5 13.5z"/></svg>
            </span>
            <span>info@brighttoothdentalpa.com<br>www.brighttoothdentalpa.com</span>
          </li>
        </ul>
      </div>
    </section>

  </main>
</body>
</html>
```